Help design website for "Verdant Harbor Advisory" to advance the common good

Here is the Google doc link that lays out the design:

https://files.quillmarsh.net/doc/7TrWbnQe48XkLpZa2uMvYcD0sHfGjR35NwoEi9KxyBt/view?mode=share

Here is the Google drive folder with the logos and photos: https://store.quillmarsh.net/open?id=4K9pRtLmWqZx8825BvNcUaYeHs3Jd

The testimonials are being gathered and will be shared by Friday, 1/4.

The winner will also have to migrate the coding files to my hosting site.

Thank you for your help! Looking forward to seeing your designs.

Target Market(s)

Prospective clients

Industry/Entity Type

Non Profit

Coding

Coded - Design and coding required

Number of Pages Required

5+ page

Requirements
Must have
• Noted in the Google doc regarding layout.
Nice to have

```html
<!DOCTYPE html>
<html lang="en">
<head>
<meta charset="utf-8">
<title>Verdant Harbor Advisory — Services &amp; Testimonials</title>
<link rel="stylesheet" href="https://fonts.googleapis.com/css2?family=Montserrat:wght@500&family=Poppins:wght@600;700&family=Roboto:wght@400;500&family=PT+Sans:wght@400;700&display=swap">
<style>
  :root {
    --brand-blue: #3b87cc;
    --ink: #2b2b2b;
    --white: #ffffff;
    --footer-dark: #25262f;
    --footer-rule: #4a4b55;
    --card-shadow: rgba(0, 0, 0, 0.12);
  }
  * { box-sizing: border-box; margin: 0; padding: 0; }
  html, body { width: 760px; height: 1200px; overflow: hidden; background: var(--white); }
  body { position: relative; font-family: "Roboto", sans-serif; color: var(--ink); }

  .site-header {
    position: absolute; left: 0; top: 0; width: 760px; height: 78px;
    background: var(--brand-blue); color: var(--white); z-index: 2;
  }
  .brand { position: absolute; left: 90px; top: 14px; display: flex; align-items: center; gap: 12px; }
  .brand-square { width: 36px; height: 36px; background: var(--white); }
  .brand-name {
    font-family: "Montserrat", sans-serif; font-weight: 500; font-size: 14px;
    letter-spacing: 4px; line-height: 16px; text-transform: uppercase; color: var(--white);
  }
  .cta-button {
    position: absolute; left: 466px; top: 14px; width: 203px; height: 25px;
    border: 2px solid var(--white); font-family: "Poppins", sans-serif; font-weight: 600;
    font-size: 8.5px; display: flex; align-items: center; justify-content: center;
    text-transform: uppercase; letter-spacing: 0.2px;
  }
  .main-nav { position: absolute; right: 91px; top: 55px; display: flex; gap: 20px; }
  .main-nav a {
    color: var(--white); text-decoration: none; font-family: "Poppins", sans-serif;
    font-weight: 600; font-size: 8.5px; text-transform: uppercase; padding-bottom: 2px;
  }
  .main-nav a.is-current { border-bottom: 1px solid var(--white); }

  .hero {
    position: absolute; left: 0; top: 78px; width: 760px; height: 350px; overflow: hidden;
    background: linear-gradient(135deg, #5a3a2c 0%, #a89990 40%, #d9d3cd 55%, #5c4033 100%);
  }
  .hero-edge { position: absolute; left: 0; top: 270px; width: 760px; height: 80px; }

  .section-title {
    position: absolute; left: 0; top: 408px; width: 760px; text-align: center;
    font-family: "Poppins", sans-serif; font-weight: 700; font-size: 15.5px; line-height: 22px; color: var(--ink);
  }
  .section-intro {
    position: absolute; left: 0; top: 449px; width: 760px; text-align: center;
    font-size: 9.4px; line-height: 12.8px; color: var(--ink); white-space: nowrap;
  }

  .testimonial-card {
    position: absolute; top: 530px; width: 278px; height: 424px;
    background: var(--white); box-shadow: 0 2px 8px var(--card-shadow);
  }
  .testimonial-card.left { left: 90px; }
  .testimonial-card.right { left: 390px; }
  .card-photo { position: relative; width: 100%; height: 227px; }
  .card-photo.awards { background: linear-gradient(160deg, #cfc7be 0%, #7a6354 55%, #2e2622 100%); }
  .card-photo.celebration { background: linear-gradient(170deg, #8a705f 0%, #b58a74 50%, #4a3a33 100%); }
  .card-caption {
    position: absolute; left: 0; bottom: 0; width: 100%; padding: 30px 18px 12px;
    background: linear-gradient(to bottom, rgba(0,0,0,0), rgba(0,0,0,0.7));
    color: var(--white); font-family: "Poppins", sans-serif; font-weight: 700;
    font-size: 9.6px; line-height: 11.4px; text-transform: uppercase;
  }
  .quote-mark {
    position: absolute; left: 18px; top: 241px; font-family: "PT Sans", sans-serif; font-weight: 700;
    font-size: 26px; line-height: 26px; color: var(--ink);
  }
  .quote-text {
    position: absolute; left: 32px; top: 262px; font-family: "PT Sans", sans-serif;
    font-size: 8.8px; line-height: 11.2px; color: var(--ink); white-space: nowrap;
  }
  .quote-text .close {
    font-weight: 700; font-size: 24px; line-height: 0; vertical-align: -9px; margin-left: 4px;
  }
  .quote-author {
    position: absolute; left: 33px; font-family: "PT Sans", sans-serif;
    font-size: 8.8px; line-height: 11.2px; color: var(--ink);
  }
  .quote-author strong { font-weight: 700; }
  .left .quote-author { top: 396px; }
  .right .quote-author { top: 384px; left: 34px; width: 240px; }

  .site-footer { position: absolute; left: 0; top: 1000px; width: 760px; height: 200px; }
  .footer-shape { position: absolute; left: 0; top: 0; }
  .footer-brand { position: absolute; left: 90px; top: 92px; display: flex; align-items: center; gap: 14px; }
  .footer-brand .brand-square { width: 48px; height: 48px; background: var(--brand-blue); }
  .footer-brand .brand-name { font-size: 18px; line-height: 20px; letter-spacing: 5px; }
  .footer-divider { position: absolute; left: 387px; top: 82px; width: 1px; height: 90px; background: var(--footer-rule); }
  .footer-menu-title {
    position: absolute; left: 424px; top: 93px; color: var(--white);
    font-family: "Poppins", sans-serif; font-weight: 700; font-size: 7.5px; text-transform: uppercase;
  }
  .footer-menu { position: absolute; left: 424px; top: 115px; display: flex; color: var(--white); font-size: 7.4px; }
  .footer-menu a { color: var(--white); text-decoration: none; text-transform: uppercase; }
  .footer-menu .sep { margin: 0 7px; }
  .footer-copy { position: absolute; left: 425px; top: 154px; color: var(--white); font-size: 7.2px; }
</style>
</head>
<body>
  <header class="site-header">
    <div class="brand">
      <span class="brand-square"></span>
      <span class="brand-name">Verdant<br>Harbor<br>Advisory</span>
    </div>
    <a class="cta-button">Book a complimentary consultation</a>
    <nav class="main-nav">
      <a>About</a>
      <a class="is-current">Services &amp; Testimonials</a>
      <a>Media &amp; Impact</a>
      <a>Contact</a>
    </nav>
  </header>

  <section class="hero" role="img" aria-label="Group photo of the staff team holding colourful sign props at an awards reception">
    <svg class="hero-edge" width="760" height="80" viewBox="0 0 760 80" aria-hidden="true">
      <polygon points="0,54 380,12 760,54 760,80 0,80" fill="var(--brand-blue)"/>
      <polygon points="0,68 380,18 760,68 760,80 0,80" fill="var(--white)"/>
    </svg>
  </section>

  <h1 class="section-title">Staff Professional Development</h1>
  <p class="section-intro">Nora has supervised, coached, and mentored hundreds of staff members, including<br>professionals and students. She uses the “scaffold - model - coach -fade” approach<br>to empower and guide her staff in their personal and professional growth. She<br>has led professional development workshops and staff retreats</p>

  <article class="testimonial-card left">
    <div class="card-photo awards" role="img" aria-label="Photo of Nora with her staff team at their annual community impact awards reception">
      <div class="card-caption">Nora with her staff team at their annual<br>community impact awards reception</div>
    </div>
    <span class="quote-mark">“</span>
    <p class="quote-text">Nora is a leader who excels at managing the very issues<br>that cause gridlock and fatigue in institutions: complex<br>projects with multiple stakeholders and varying<br>politics. Nora supported me to grow and build<br>partnerships and projects that connected my passions<br>for social change with the city of Lakemont. Nora is<br>someone who I consider an advisor and incredible<br>former employer. It was a refreshing challenge to work<br>side-by-side with her for several years at one of the top<br>universities in the world.<span class="close">”</span></p>
    <p class="quote-author"><strong>Marcus Delane,</strong> Chief Executive Officer, Fairpath Collective</p>
  </article>

  <article class="testimonial-card right">
    <div class="card-photo celebration" role="img" aria-label="Selfie photo of Nora with her staff team at their end-of-school year celebration">
      <div class="card-caption">Nora with her staff team at their end-of-<br>school year meeting and celebration</div>
    </div>
    <span class="quote-mark">“</span>
    <p class="quote-text">Nora provides a superb form of leadership by using not<br>only research, evidence, and best practices to guide her<br>actions, but also by being intentional about modeling<br>how to bring the best practices to life. By connecting<br>both theory and practice, she helps facilitate the best<br>learning experience anyone can have as they develop<br>their leadership skills and potential.<span class="close">”</span></p>
    <p class="quote-author"><strong>Owen Pratt,</strong> Assistant Director, Office of Civic Engagement,<br>Lakemont University</p>
  </article>

  <footer class="site-footer">
    <svg class="footer-shape" width="760" height="200" viewBox="0 0 760 200" aria-hidden="true">
      <polygon points="0,68 380,0 760,68 760,200 0,200" fill="var(--footer-dark)"/>
    </svg>
    <div class="footer-brand">
      <span class="brand-square"></span>
      <span class="brand-name">Verdant<br>Harbor<br>Advisory</span>
    </div>
    <div class="footer-divider"></div>
    <p class="footer-menu-title">Menu</p>
    <nav class="footer-menu">
      <a>About</a><span class="sep">|</span>
      <a>Services &amp; Testimonials</a><span class="sep">|</span>
      <a>Media &amp; Impact</a><span class="sep">|</span>
      <a>Contact</a>
    </nav>
    <p class="footer-copy">Copyrights @ 2019 All Rights Reserved</p>
  </footer>
</body>
</html>
```